Design the World's Greatest Valentine's Day Greeting Card

We're looking for designers who can create the best Valentine's Day greeting card designs in the world. Your design could be could be extra special because it is funny, beautiful, inspiring or original.

Your designs should be able to fit on a standard 4"x6" greeting card. The main design will need to be for the front page (cover) of the card, but you can also include some design for the inside pages if you like.

Multiple winners will be awarded, and will be chosen within 5 days after the contest ends on February 13, 2019.
First Prize: $200
Runners-up: $100 each

The winning card design (or designs) could be recognised as standout designs publicly, as they can be used, by Gigmarten.com, at it sole discretion, in some Gigmarten.com marketing or PR materials.

Let's celebrate Valentine's Day together by showcasing your designs!

```html
<!DOCTYPE html>
<html lang="en">
<head>
<meta charset="utf-8">
<title>Happy Valentine's Day Card</title>
<link href="https://fonts.googleapis.com/css2?family=Archivo+Black&family=Oswald:wght@300;600&family=Dancing+Script:wght@500&display=swap" rel="stylesheet">
<style>
  :root {
    --page: #ffffff;
    --card-dark: #0d0808;
    --skin-warm: #c0603a;
    --skin-deep: #5a1d12;
    --band: rgba(255, 255, 255, 0.72);
    --heart-red: #e01e3c;
    --heart-black: #000000;
    --heart-cream: #e8c8b5;
    --ink-white: #ffffff;
    --ink-grey: #e6e6e6;
    --letter-shadow: #000000;
  }
  html, body {
    margin: 0;
    padding: 0;
    width: 811px;
    height: 1200px;
    overflow: hidden;
    background: var(--page);
  }
  .card {
    position: relative;
    width: 811px;
    height: 1200px;
    background: var(--page);
  }
  .card-face {
    position: absolute;
    left: 9px;
    top: 7px;
    width: 793px;
    height: 1179px;
    border-radius: 6px;
    overflow: hidden;
    background: var(--card-dark);
  }
  .hands-photo {
    position: absolute;
    left: 0;
    top: 0;
    width: 793px;
    height: 640px;
    background:
      radial-gradient(ellipse 60% 55% at 62% 45%, var(--skin-warm) 0%, #8a3a22 45%, var(--skin-deep) 75%, transparent 100%),
      linear-gradient(180deg, #3a120c 0%, #2a0d08 80%, var(--card-dark) 100%);
  }
  .title-band {
    position: absolute;
    left: 56px;
    top: 0;
    width: 117px;
    height: 1179px;
    background: var(--band);
  }
  .title-word {
    position: absolute;
    margin: 0;
    width: 90px;
    font-family: "Archivo Black", "Anton", sans-serif;
    font-weight: 400;
    color: var(--heart-red);
    text-align: center;
    text-shadow:
      -2px 0 0 var(--ink-white), 2px 0 0 var(--ink-white), 0 -2px 0 var(--ink-white), 0 2px 0 var(--ink-white),
      -8px 2px 0 var(--letter-shadow), -6px 2px 0 var(--letter-shadow), -4px 1px 0 var(--letter-shadow);
  }
  .title-word .letter {
    position: relative;
    display: block;
    white-space: nowrap;
  }
  .word-happy { left: 45px; top: 11px; font-size: 76px; }
  .word-happy .letter { height: 68px; line-height: 68px; }
  .word-valentines { left: 112px; top: 353px; font-size: 70px; }
  .word-valentines .letter { height: 62px; line-height: 62px; }
  .word-day { left: 45px; top: 978px; font-size: 70px; }
  .word-day .letter { height: 63px; line-height: 63px; }
  .apostrophe {
    position: absolute;
    right: -14px;
    top: -18px;
    font-size: 56px;
  }
  .art {
    position: absolute;
    left: 0;
    top: 0;
  }
  .message {
    position: absolute;
    left: 240px;
    top: 812px;
    width: 553px;
    text-align: center;
  }
  .message-lead {
    margin: 0 0 0 -18px;
    font-family: "Oswald", sans-serif;
    font-size: 60px;
    letter-spacing: 0;
    color: var(--ink-grey);
    font-weight: 300;
    line-height: 1;
  }
  .message-lead strong { font-weight: 600; color: var(--ink-white); }
  .message-main {
    margin: 0 0 0 10px;
    font-family: "Dancing Script", cursive;
    font-weight: 500;
    font-size: 134px;
    color: var(--heart-red);
    line-height: 1.05;
    white-space: nowrap;
  }
</style>
</head>
<body>
<div class="card">
  <div class="card-face">
    <div class="hands-photo" role="img" aria-label="Photo of two hands forming a heart shape against a dark background"></div>
    <div class="title-band"></div>

    <svg class="art" width="793" height="1179" viewBox="0 0 793 1179" aria-hidden="true">
      <defs>
        <path id="heart" d="M50 90 C22 62 0 48 0 26 C0 10 12 0 27 0 C38 0 46 6 50 16 C54 6 62 0 73 0 C88 0 100 10 100 26 C100 48 78 62 50 90Z"/>
      </defs>
      <use href="#heart" fill="var(--heart-black)" transform="translate(275 151) scale(4.86 4.86)"/>
      <use href="#heart" fill="var(--heart-red)" transform="translate(315 241) scale(3.96 3.75)"/>
      <use href="#heart" fill="var(--heart-cream)" transform="translate(342 272) scale(3.42 3.4)"/>
      <g class="arrow" transform="translate(338 1053)">
        <line x1="20" y1="0" x2="292" y2="0" stroke="var(--ink-white)" stroke-width="3"/>
        <polygon points="292,-10 314,0 292,10" fill="var(--ink-white)"/>
        <g fill="none" stroke="var(--ink-white)" stroke-width="3">
          <polyline points="0,-11 10,0 0,11"/>
          <polyline points="12,-11 22,0 12,11"/>
          <polyline points="24,-11 34,0 24,11"/>
        </g>
        <use href="#heart" fill="var(--heart-red)" transform="translate(142 -17) scale(0.34 0.38)"/>
      </g>
    </svg>

    <h1 class="title-word word-happy">
      <span class="letter">H</span><span class="letter">A</span><span class="letter">P</span><span class="letter">P</span><span class="letter">Y</span>
    </h1>
    <h1 class="title-word word-valentines">
      <span class="letter">V</span><span class="letter">A</span><span class="letter">L</span><span class="letter">E</span><span class="letter">N</span><span class="letter">T</span><span class="letter">I</span><span class="letter">N</span><span class="letter">E<span class="apostrophe">’</span></span><span class="letter">S</span>
    </h1>
    <h1 class="title-word word-day">
      <span class="letter">D</span><span class="letter">A</span><span class="letter">Y</span>
    </h1>

    <div class="message">
      <p class="message-lead">I WILL <strong>ALWAYS</strong></p>
      <p class="message-main">Love You</p>
    </div>
  </div>
</div>
</body>
</html>
```